Business card for my company-RKV Design Studio

I do not have a logo-I like red and keeping it clean. Information that should be on the card:
Tom Brazenhall AIA
Architecture Planning Interiors
Cell Phone-614.529.4086
email-rkvplanner4@mailvane.net
www.rkvdesignstudio.net

```html
<!DOCTYPE html>
<html lang="en">
<head>
<meta charset="utf-8">
<title>RKV Design Studio — Business Card</title>
<link href="https://fonts.googleapis.com/css2?family=Poppins:wght@300;400;700;800&display=swap" rel="stylesheet">
<style>
  :root {
    --brand-red: #e31e26;
    --ink: #111111;
    --paper: #f7f7f6;
    --backdrop: #ececeb;
    --white: #ffffff;
  }
  * { margin: 0; padding: 0; box-sizing: border-box; }
  html, body {
    width: 1200px; height: 721px; overflow: hidden;
    background: var(--backdrop);
    font-family: "Poppins", sans-serif;
  }
  .canvas { position: relative; width: 1200px; height: 721px; }

  .card {
    position: absolute;
    width: 500px; height: 286px;
    overflow: hidden;
    box-shadow: 0 10px 30px rgba(0,0,0,0.12);
  }

  /* Front — contact side */
  .card-front { left: 70px; top: 218px; background: var(--paper); }
  .front-disc {
    position: absolute; left: 18px; top: -2px;
    width: 150px; height: 150px; border-radius: 50%;
    background: var(--brand-red);
  }
  .front-slash {
    position: absolute; left: 112px; top: 58px;
    width: 2px; height: 52px; background: var(--white);
    transform: rotate(14deg);
  }
  .person-name {
    position: absolute; left: 124px; top: 79px;
    font-size: 23px; font-weight: 800; letter-spacing: 2px;
    color: var(--ink); white-space: nowrap;
  }
  .name-rule {
    position: absolute; left: 150px; top: 114px;
    width: 266px; height: 1.5px; background: var(--ink);
  }
  .disciplines {
    position: absolute; left: 152px; top: 120px;
    font-size: 11px; font-weight: 400; letter-spacing: 1.6px;
    color: var(--ink); white-space: nowrap;
  }
  .contact-list {
    position: absolute; left: 36px; top: 186px;
    list-style: none;
    font-size: 11.5px; font-weight: 300; letter-spacing: 1.4px;
    color: var(--ink); line-height: 19px;
  }
  .accent-line { position: absolute; left: 0; top: 0; }
  .website {
    position: absolute; left: 478px; top: 143px;
    transform: translate(-50%, -50%) rotate(-90deg);
    font-size: 11px; font-weight: 400; letter-spacing: 1.5px;
    color: var(--ink); white-space: nowrap;
  }

  /* Back — studio side */
  .card-back { left: 630px; top: 218px; background: var(--brand-red); }
  .studio-mark {
    position: absolute; left: 118px; top: 82px;
    width: 112px; height: 112px; border-radius: 50%;
    background: var(--white);
  }
  .studio-name {
    position: absolute; left: 250px; top: 92px;
    font-size: 27px; font-weight: 400; line-height: 31px;
    letter-spacing: 1.5px; color: var(--white);
  }
</style>
</head>
<body>
<main class="canvas">

  <section class="card card-front" aria-label="Business card, contact side">
    <div class="front-disc"></div>
    <div class="front-slash"></div>
    <h1 class="person-name">TOM BRAZENHALL AIA</h1>
    <div class="name-rule"></div>
    <p class="disciplines">ARCHITECTURE PLANNING INTERIORS</p>
    <ul class="contact-list">
      <li>CELL - 614.529.4086</li>
      <li>RKVPLANNER4@MAILVANE.NET</li>
    </ul>
    <svg class="accent-line" width="500" height="286" viewBox="0 0 500 286" aria-hidden="true">
      <circle cx="372" cy="248" r="22" fill="var(--brand-red)"/>
      <line x1="200" y1="232" x2="430" y2="268" stroke="var(--ink)" stroke-width="1"/>
    </svg>
    <p class="website">WWW.RKVDESIGNSTUDIO.NET</p>
  </section>

  <section class="card card-back" aria-label="Business card, studio side">
    <div class="studio-mark"></div>
    <p class="studio-name">RKV<br>DESIGN<br>STUDIO</p>
  </section>

</main>
</body>
</html>
```